" O estabelecimento deverá funcionar como um centro de desenvolvimento humano, como foco em hipnoterapia, destinada à pessoas que desejam tratar todo tipo de doença de origem emocional (ansiedade, depressão, medo, fobia, fibromialgia, dores crônicas, diabetes, etc.), bem como pessoas que desejam potencializar seus resultados no âmbito profissional e financeiro, através de técnicas utilizadas na PNL (Programação Neurolinguística), mudança de hábitos e comportamento, transformação pessoal. Também funcionará como um centro de cursos e formação de novos profissionais hipnoterapeutas com um método exclusivo chamado Torvalune. "

```html
<!DOCTYPE html>
<html lang="pt-BR">
<head>
<meta charset="UTF-8">
<title>Torvalune – Assinatura de e-mail</title>
<link href="https://fonts.googleapis.com/css2?family=Montserrat:wght@400;500;600;700&display=swap" rel="stylesheet">
<style>
  :root {
    --teal: #5a9e8e;
    --teal-faint: #e3efec;
    --ink: #1d1d1b;
    --paper: #ffffff;
    --backdrop: #eeeeee;
  }
  * { margin: 0; padding: 0; box-sizing: border-box; }
  html, body { width: 1200px; height: 1200px; overflow: hidden; }
  body {
    background: var(--backdrop);
    font-family: "Montserrat", sans-serif;
    color: var(--ink);
    position: relative;
  }
  .signature {
    position: absolute;
    left: 96px; top: 473px;
    width: 1008px; height: 276px;
    background: var(--paper);
    overflow: hidden;
  }
  .signature__shapes { position: absolute; inset: 0; }
  .brand {
    position: absolute;
    left: 90px; top: 30px;
    width: 240px;
    text-align: center;
  }
  .brand__dot {
    width: 120px; height: 120px;
    border-radius: 50%;
    background: var(--teal);
    margin: 0 auto 24px;
  }
  .brand__name {
    font-size: 40px; font-weight: 600;
    color: var(--ink);
    letter-spacing: 0.5px;
  }
  .contact {
    position: absolute;
    left: 552px; top: 30px;
  }
  .contact__name {
    font-size: 25px; font-weight: 500;
    color: var(--teal);
    letter-spacing: 0.5px;
    line-height: 1;
  }
  .contact__role {
    font-size: 12px; font-weight: 700;
    margin-top: 6px;
    text-transform: uppercase;
  }
  .contact__list { list-style: none; margin-top: 14px; }
  .contact__item {
    display: flex; align-items: center;
    gap: 16px;
    font-size: 12.5px; line-height: 17px;
    margin-bottom: 12px;
  }
  .contact__icon { width: 20px; height: 20px; flex: none; fill: var(--ink); }
  .contact__item b { font-weight: 700; }
</style>
</head>
<body>
  <section class="signature">
    <svg class="signature__shapes" viewBox="0 0 1008 276" aria-hidden="true">
      <circle cx="905" cy="110" r="88" fill="none" stroke="var(--teal-faint)" stroke-width="14"/>
      <path d="M500 0 H545 C470 70 450 170 470 276 H440 C415 170 430 70 500 0 Z" fill="var(--teal)"/>
      <path d="M432 100 C410 150 410 210 425 276 H440 C420 210 418 150 432 100 Z" fill="var(--ink)"/>
    </svg>

    <div class="brand">
      <div class="brand__dot"></div>
      <div class="brand__name">Torvalune</div>
    </div>

    <div class="contact">
      <h1 class="contact__name">NOME COMPLETO</h1>
      <p class="contact__role">Cargo ou função</p>
      <ul class="contact__list">
        <li class="contact__item">
          <svg class="contact__icon" viewBox="0 0 24 24"><path d="M6.6 10.8a15 15 0 0 0 6.6 6.6l2.2-2.2c.3-.3.7-.4 1-.2 1.1.4 2.3.6 3.6.6.6 0 1 .4 1 1V20c0 .6-.4 1-1 1A17 17 0 0 1 3 4c0-.6.4-1 1-1h3.5c.6 0 1 .4 1 1 0 1.3.2 2.5.6 3.6.1.3 0 .7-.2 1z"/></svg>
          <span>00 0000.00000<br>00 0000.00000</span>
        </li>
        <li class="contact__item">
          <svg class="contact__icon" viewBox="0 0 24 24"><path d="M12 2a10 10 0 1 0 0 20 10 10 0 0 0 0-20zm6.9 6h-2.9a15.7 15.7 0 0 0-1.4-3.6A8 8 0 0 1 18.9 8zM12 4c.8 1.2 1.5 2.5 1.9 4h-3.8c.4-1.5 1.1-2.8 1.9-4zM4.3 14a8 8 0 0 1 0-4h3.4a16 16 0 0 0 0 4zm.8 2h2.9c.3 1.3.8 2.5 1.4 3.6A8 8 0 0 1 5.1 16zM8 8H5.1a8 8 0 0 1 4.3-3.6C8.8 5.5 8.3 6.7 8 8zm4 12c-.8-1.2-1.5-2.5-1.9-4h3.8c-.4 1.5-1.1 2.8-1.9 4zm2.3-6H9.7a14.7 14.7 0 0 1 0-4h4.6a14.7 14.7 0 0 1 0 4zm.3 5.6c.6-1.1 1.1-2.3 1.4-3.6h2.9a8 8 0 0 1-4.3 3.6zm1.7-5.6a16 16 0 0 0 0-4h3.4a8 8 0 0 1 0 4z"/></svg>
          <span><b>torvalune.com.br</b><br>contato@torvalune.com.br</span>
        </li>
        <li class="contact__item">
          <svg class="contact__icon" viewBox="0 0 24 24"><path d="M12 2a7 7 0 0 0-7 7c0 5.2 7 13 7 13s7-7.8 7-13a7 7 0 0 0-7-7zm0 9.5a2.5 2.5 0 1 1 0-5 2.5 2.5 0 0 1 0 5z"/></svg>
          <span>Nome da <b>rua</b>, 000 - bairro<br><b>cidade</b> - estado - <b>cep</b> e país</span>
        </li>
      </ul>
    </div>
  </section>
</body>
</html>
```